Schriftdesign für Shop-Header Bild (Schmuckhandel) / Online-Marketing Material
Zielgruppe
Wir verkaufen Schmuck im Onlineshop mit Herz
Aufgabenstellung
Wir benötigen den vorgegebenen Text in schöner Form, Farbe und Größe harmonisch eingefügt, in unserem Bild.
Folgender Text soll sich schick ins Bild einfügen oder in 3-D vielleicht in Schriftfarbe gold hervorheben:
Mit ganzem Herzen für Sie da!
Ihr Online -Juwelier mit Herz
Siehe auch unser altes Bild mit Text, im Shop, wie es nicht aussehen sollte: www.lindenglanzhof.de

```html
<!DOCTYPE html>
<html lang="de">
<head>
<meta charset="utf-8">
<title>Lindenglanzhof – Ihr Online-Juwelier mit Herz</title>
<link rel="stylesheet" href="https://fonts.googleapis.com/css2?family=Lato:wght@400;700&family=Questrial&family=Lobster&family=Handlee&display=swap">
<style>
  :root {
    --red: #d81f26;
    --red-text: #c8161d;
    --salmon: #e9756b;
    --ink: #1d1d1d;
    --gray: #6f6f6f;
    --nav-bg: #666266;
    --field-bg: #efefef;
    --gold-light: #fff1bd;
    --gold: #e4b54e;
    --gold-deep: #a8741f;
    --gold-edge: #6e4210;
    --gold-shadow: #4a2a08;
    --dot: #d6d6d6;
  }
  * { box-sizing: border-box; margin: 0; padding: 0; }
  html, body { width: 1200px; height: 855px; overflow: hidden; background: #fff; }
  body { position: relative; font-family: "Lato", sans-serif; color: var(--ink); }

  .meta-nav { position: absolute; top: 6px; right: 230px; display: flex; gap: 15px; font-size: 9px; }
  .meta-nav a { color: var(--ink); text-decoration: none; }
  .meta-nav a.is-active { color: var(--red); }

  .brand { position: absolute; left: 232px; top: 30px; display: flex; align-items: center; gap: 6px; }
  .brand-dot { width: 12px; height: 12px; border-radius: 50%; background: var(--red); }
  .brand-name { font-family: "Lato", sans-serif; font-weight: 700; font-size: 15px; color: var(--red); }

  .search-label { position: absolute; left: 421px; top: 25px; font-size: 12.5px; }
  .search-label::after { content: ""; display: inline-block; margin-left: 7px; border: 4.5px solid transparent; border-top: 5px solid var(--red); vertical-align: -2px; }
  .search-field { position: absolute; left: 421px; top: 47px; width: 320px; height: 30px; background: var(--field-bg); }
  .search-field span { position: absolute; left: 19px; top: 8px; font-size: 10.5px; color: #888; }
  .search-field svg { position: absolute; right: 7px; top: 5px; }
  .cart { position: absolute; left: 783px; top: 47px; width: 187px; height: 31px; background: var(--field-bg); }
  .cart span { position: absolute; left: 19px; top: 9px; font-size: 10.5px; color: var(--salmon); }
  .cart svg { position: absolute; right: 16px; top: 5px; }

  .main-nav { position: absolute; left: 0; top: 104px; width: 1200px; height: 33px; background: var(--nav-bg); }
  .main-nav .notch { position: absolute; left: 248px; top: 0; }
  .main-nav ul { list-style: none; position: absolute; left: 324px; top: 9px; display: flex; gap: 29px; font-family: "Questrial", sans-serif; font-size: 12.5px; color: #fff; }

  .hero { position: absolute; left: 0; top: 137px; width: 1200px; height: 298px; background: linear-gradient(115deg, #ecebe7 0%, #e4e1dc 35%, #f0e6d6 60%, #e5cfae 85%, #d8b88c 100%); }
  .hero-visual { position: absolute; left: 455px; top: 60px; width: 215px; height: 215px; border-radius: 50%; background: radial-gradient(circle, #e6c57c 0%, #d4a64f 55%, rgba(212,166,79,0) 72%); }
  .hero-line {
    position: absolute;
    display: inline-block;
    font-family: "Lobster", cursive;
    font-weight: 400;
    font-size: 32px;
    line-height: 1.15;
    white-space: nowrap;
    color: transparent;
    background: linear-gradient(180deg, var(--gold-light) 0%, var(--gold) 42%, var(--gold-deep) 58%, #f2cf76 82%, var(--gold) 100%);
    -webkit-background-clip: text;
    background-clip: text;
    -webkit-text-stroke: 0.5px var(--gold-edge);
    filter: drop-shadow(1px 1px 0 var(--gold-edge)) drop-shadow(1px 1px 0 var(--gold-shadow)) drop-shadow(1px 2px 2px rgba(60, 30, 5, .45));
  }
  .hero-line.top { left: 224px; top: 12px; }
  .hero-line.bottom { left: 607px; top: 227px; }
  .hero-shade { position: absolute; left: 0; top: 435px; width: 1200px; height: 16px; background: linear-gradient(#e9e4e2, #fff); }

  .store-teaser { position: absolute; left: 230px; top: 534px; font-size: 14px; color: var(--gray); }
  .store-teaser small { font-size: 12px; }
  .store-banner { position: absolute; left: 230px; top: 569px; width: 466px; height: 156px; background: linear-gradient(90deg, #262626 0%, #3a3a3a 50%, #8a5a30 72%, #5e5e5e 100%); box-shadow: 0 0 3px rgba(0,0,0,.35); }
  .slider-dots { position: absolute; right: 20px; bottom: 10px; display: flex; gap: 7px; }
  .slider-dots i { width: 8px; height: 8px; border-radius: 50%; background: #fff; }
  .slider-dots i.is-current { background: var(--red); }

  .trust { position: absolute; left: 727px; top: 461px; width: 243px; }
  .seal { position: relative; height: 66px; }
  .seal .disc { position: absolute; left: 12px; top: 0; width: 64px; height: 64px; border-radius: 50%; background: #243a7a; border: 4px solid #c9a84a; }
  .seal .ribbon { position: absolute; left: 66px; top: 19px; width: 54px; height: 25px; background: #d9b95a; }
  .divider { height: 0; border-top: 4px dotted var(--dot); margin-top: 9px; }
  .benefits { list-style: none; margin: 14px 0 10px; }
  .benefits li { display: flex; align-items: center; gap: 7px; height: 30px; font-size: 12.5px; color: var(--red-text); padding-left: 3px; }

  .welcome { position: absolute; left: 230px; top: 771px; font-family: "Handlee", cursive; font-weight: 400; font-size: 20px; color: var(--gray); }
  .welcome em { font-style: normal; color: var(--red-text); }
  .tagline { position: absolute; left: 230px; top: 817px; font-size: 15px; font-weight: 700; color: var(--gray); }
</style>
</head>
<body>
  <nav class="meta-nav">
    <a class="is-active" href="#">Startseite</a>
    <a href="#">Anmelden</a>
    <a href="#">Mein Konto</a>
    <a href="#">Newsletter abonnieren</a>
    <a href="#">Kontakt</a>
  </nav>

  <div class="brand"><span class="brand-dot"></span><span class="brand-name">Lindenglanzhof</span></div>

  <div class="search-label">Nach welchem Artikel suchen Sie?</div>
  <div class="search-field">
    <span>Suchen nach</span>
    <svg width="22" height="20" viewBox="0 0 22 20"><circle cx="11" cy="10" r="9.5" fill="var(--red)"/><circle cx="10" cy="9" r="3.2" fill="none" stroke="#fff" stroke-width="1.6"/><line x1="12.3" y1="11.3" x2="15" y2="14" stroke="#fff" stroke-width="1.8"/></svg>
  </div>
  <div class="cart">
    <span>Ihr Warenkorb ist leer.</span>
    <svg width="16" height="20" viewBox="0 0 16 20"><path d="M5 6V4a3 3 0 0 1 6 0v2" fill="none" stroke="var(--red)" stroke-width="1.5"/><rect x="0" y="6" width="16" height="14" rx="1" fill="var(--red)"/><path d="M8 16l-3-3a1.6 1.6 0 0 1 3-1.6A1.6 1.6 0 0 1 11 13z" fill="#fff"/></svg>
  </div>

  <nav class="main-nav">
    <svg class="notch" width="62" height="22" viewBox="0 0 62 22"><polygon points="0,0 62,0 31,22" fill="#fff"/></svg>
    <ul>
      <li>KREUZ-ANHÄNGER</li>
      <li>ANHÄNGER/VERSCH.</li>
      <li>FOTO-MEDAILLONS</li>
      <li>OHRSCHMUCK</li>
      <li>ACCESSOIRES</li>
    </ul>
  </nav>

  <header class="hero">
    <div class="hero-visual" role="img" aria-label="Foto: goldener Herzanhänger an Kette auf cremefarbener Seide"></div>
    <h1 class="hero-line top">Mit ganzem Herzen für Sie da!</h1>
    <p class="hero-line bottom">Ihr Online -Juwelier mit Herz</p>
  </header>
  <div class="hero-shade"></div>

  <p class="store-teaser">Besuchen Sie auch unseren AURIVANE-Schmuck Store: <small>hier</small></p>
  <div class="store-banner" role="img" aria-label="Banner des AURIVANE-Schmuck Stores: Goldschmelze über Flamme, Hinweis auf Herstellung in Deutschland">
    <div class="slider-dots"><i></i><i></i><i class="is-current"></i><i></i><i></i><i></i></div>
  </div>

  <aside class="trust">
    <div class="seal"><span class="ribbon"></span><span class="disc"></span></div>
    <div class="divider"></div>
    <ul class="benefits">
      <li><svg width="24" height="22" viewBox="0 0 24 22"><path d="M12 20L3 11a5 5 0 0 1 9-6 5 5 0 0 1 9 6z" fill="#f7c3c6" stroke="var(--red)" stroke-width="1.3"/></svg>Versand innerhalb von 24 Stunden</li>
      <li><svg width="24" height="22" viewBox="0 0 24 22"><path d="M12 20L3 11a5 5 0 0 1 9-6 5 5 0 0 1 9 6z" fill="#f7c3c6" stroke="var(--red)" stroke-width="1.3"/></svg>schneller, persönlicher Service</li>
      <li><svg width="24" height="22" viewBox="0 0 24 22"><path d="M12 20L3 11a5 5 0 0 1 9-6 5 5 0 0 1 9 6z" fill="#f7c3c6" stroke="var(--red)" stroke-width="1.3"/></svg>Kundenzufriedenheit an erster Stelle</li>
      <li><svg width="24" height="22" viewBox="0 0 24 22"><path d="M12 20L3 11a5 5 0 0 1 9-6 5 5 0 0 1 9 6z" fill="#f7c3c6" stroke="var(--red)" stroke-width="1.3"/></svg>sichere Zahlungsmethoden</li>
    </ul>
    <div class="divider"></div>
  </aside>

  <h2 class="welcome">Herzlich Willkommen im <em>Lindenglanzhof.de</em> Schmuck-Shop</h2>
  <p class="tagline">Ihr Online-Juwelier mit Herz</p>
</body>
</html>
```